independent cleaner, reliable, custom, thorough, trustworthy

Not sure yet if I want single-sided or double sided, so I'm selecting double-sided just in case, but single-sided designs are okay.

Really looking to find the happy medium between personal and professional in a business card design. I end up building comfortable relationships with the people I work for.

Most of my business is through referrals, but I want some business cards to hand out to people who ask for one (and maybe put them on community bulletin boards).

My target market is homeowners and business owners who are looking for a reliable cleaner and are willing to pay a bit more to have excellent quality and someone they trust.

Theme: I have a personal-professional feel since I'm solo, so the theme should reflect that. Trustworthy, personal, simple. I clean up messes.

Hopefully this is enough info, let me know if you have any questions though of course!

Target Market(s)

Homeowners businessowners who are looking for a reliable cleaner, excellent quality trustworthy.

Industry/Entity Type

Cleaning Service

Contact Information for Business Card

Please include this text:
• Delphine Marrow
• independent cleaner
• reliable, custom, thorough
• 604-317-2296
• tbw.marrow@quillpost.net

Font styles to use
Serif
Sans Serif

Colors
ffffff
00a990
0492cd
33a6d7
0355a3
3276b5
919191

Requirements
Must have
• Really looking to find the happy medium between personal and professional in a business card design.
• Background: at least 50% white on the side with the most text (coloured accents or shapes are okay)
• I lean more towards simple and clean, solid colours, maybe a gentle gradient
Nice to have
• Not sure yet if I want single-sided or double sided, so I'm selecting double-sided just in case, but single-sided designs are okay.
• Colours: preferably blues and teals for the font and other objects (if any). Open to designer's choice though. I've toyed around with orangey-yellow, but it doesn't feel right and I keep going back to blues/teals
• Also I uploaded a sketch of my signature and initials so you can get a feel for my personality. I'm not expecting this to be included in the design, it's just there.
Should not have
• I don't like a lot of busy-ness or textures
• Also I don't have a logo (not sure where else to specify this)

```html
<!DOCTYPE html>
<html lang="en">
<head>
<meta charset="utf-8">
<title>Delphine Marrow – Business Card</title>
<link rel="stylesheet" href="https://fonts.googleapis.com/css2?family=Roboto:wght@400;500&display=swap">
<style>
  :root {
    --page-bg: #d8d3cb;
    --card-frost: #ecebe8;
    --card-frost-edge: #dcdad6;
    --teal-dark: #0c6f5c;
    --teal-mid: #12876f;
    --teal-light: #1c9a80;
    --edge-grey: #8c8c8c;
    --text-cream: #efe6d6;
    --signature-tone: #0f6b4f;
  }
  * { margin: 0; padding: 0; box-sizing: border-box; }
  html, body {
    width: 1200px;
    height: 970px;
    overflow: hidden;
    background: var(--page-bg);
    font-family: "Roboto", Arial, sans-serif;
  }
  .business-card {
    position: absolute;
    left: 100px;
    top: 200px;
    width: 1000px;
    height: 570px;
    border-radius: 26px;
    overflow: hidden;
    box-shadow: 0 18px 40px rgba(0,0,0,0.18);
  }
  .card-shapes {
    position: absolute;
    inset: 0;
    width: 1000px;
    height: 570px;
  }
  .card-identity {
    position: absolute;
    left: 62px;
    top: 128px;
    color: var(--text-cream);
  }
  .card-name {
    font-size: 29px;
    font-weight: 500;
    letter-spacing: 0.5px;
    line-height: 1.1;
    text-transform: uppercase;
  }
  .card-role {
    font-size: 23px;
    font-weight: 400;
    letter-spacing: 0.4px;
    line-height: 1.2;
  }
  .card-contacts {
    position: absolute;
    left: 62px;
    top: 275px;
    list-style: none;
    color: var(--text-cream);
    font-size: 24px;
  }
  .contact-item {
    display: flex;
    align-items: center;
    gap: 12px;
    height: 33px;
  }
  .contact-icon { width: 28px; height: 28px; flex: none; }
  .card-tagline {
    position: absolute;
    left: 62px;
    top: 377px;
    color: var(--text-cream);
    font-size: 24px;
    letter-spacing: 0.2px;
  }
  .signature-area {
    position: absolute;
    left: 566px;
    top: 178px;
    width: 340px;
    height: 206px;
    border-radius: 18px;
    background: radial-gradient(ellipse at center, rgba(15,107,79,0.22), rgba(15,107,79,0.04) 70%, rgba(15,107,79,0) 100%);
  }
</style>
</head>
<body>
  <section class="business-card" aria-label="Business card for Delphine Marrow, independent cleaner">
    <svg class="card-shapes" viewBox="0 0 1000 570" aria-hidden="true">
      <defs>
        <linearGradient id="tealPanel" x1="0" y1="0" x2="1" y2="1">
          <stop offset="0" stop-color="var(--teal-mid)"/>
          <stop offset="0.45" stop-color="var(--teal-light)"/>
          <stop offset="1" stop-color="var(--teal-dark)"/>
        </linearGradient>
        <linearGradient id="frostPanel" x1="0" y1="0" x2="1" y2="1">
          <stop offset="0" stop-color="var(--card-frost)"/>
          <stop offset="1" stop-color="var(--card-frost-edge)"/>
        </linearGradient>
      </defs>
      <rect class="frost-panel" width="1000" height="570" fill="url(#frostPanel)"/>
      <path class="edge-shadow" d="M548 0 Q448 285 546 570" fill="none" stroke="var(--edge-grey)" stroke-width="6" opacity="0.7"/>
      <path class="teal-panel" d="M0 0 H530 Q430 285 528 570 H0 Z" fill="url(#tealPanel)"/>
      <circle class="card-notch" cx="0" cy="155" r="24" fill="var(--card-frost)"/>
    </svg>

    <div class="card-identity">
      <h1 class="card-name">Delphine Marrow</h1>
      <p class="card-role">independent cleaner</p>
    </div>

    <ul class="card-contacts">
      <li class="contact-item">
        <svg class="contact-icon" viewBox="0 0 28 28" aria-hidden="true">
          <circle cx="14" cy="14" r="12.5" fill="none" stroke="var(--text-cream)" stroke-width="2"/>
          <path d="M10 8.5 L12 8 L13.3 11 L12 12.2 Q13 14.8 15.8 16 L17 14.7 L20 16 L19.5 18 Q17.5 19.8 14 17.8 Q10.4 15.6 9 12 Q8.3 10 10 8.5 Z" fill="var(--text-cream)"/>
        </svg>
        <span class="contact-text">604-317-2296</span>
      </li>
      <li class="contact-item">
        <svg class="contact-icon" viewBox="0 0 28 28" aria-hidden="true">
          <circle cx="14" cy="14" r="12.5" fill="none" stroke="var(--text-cream)" stroke-width="2"/>
          <rect x="7.5" y="9.5" width="13" height="9" rx="1" fill="none" stroke="var(--text-cream)" stroke-width="1.6"/>
          <path d="M7.8 10 L14 15 L20.2 10" fill="none" stroke="var(--text-cream)" stroke-width="1.6"/>
        </svg>
        <span class="contact-text">tbw.marrow@quillpost.net</span>
      </li>
    </ul>

    <p class="card-tagline">Reliable | Custom | Thorough</p>

    <div class="signature-area" role="img" aria-label="Handwritten surname signature in dark green script"></div>
  </section>
</body>
</html>
```